Professional, polished website design for boutique wealth management firm

Hello, thank you for your interest. PLEASE READ THE BRIEF BEFORE SUBMITTING THE DESIGN.-
PLEASE USE THE ATTACHED HOME PAGE COPY FOR THIS DESIGN.
We are looking for a professional, polished design that helps portray trust and credibility for a well-established independent wealth management firm. We have copy we've written for the home page and we'd like the design and imagery to play up the copy, so there's a better chance someone will read it all. So the headlines etc should all be easy to read and the design should draw the eye towards them. For colors, again trust is important so probably blue as a dominant color, but you can also use gray, green, etc. We'd like to avoid too much use of the color red (due to financial, association with loss). SO PLEASE AVOID USE OF THE COLOR RED. We also like bright orange or yellow for call to action buttons.

Please keep the design EASY TO MAINTAIN in wordpress as well.

I have attached home page copy as well as logo files.

Here's some sites that we like so feel free to use as inspiration:
https://www.brovaltcapitalworks.example/, https://harborpathpensionsplains.example/
https://tavrin-oakes.example/, https://plantfornextyear.example/, https://ferngatefinancial.example/

As another option/idea, I like the idea of a simple format with a clean image similar to this for the home page: https://www.pixmeadowstock.example/detail/photo/calculator-falling-royalty-free-image/31684207?adppopup=true
Just an idea.

Also please be sure to incorporate the QWA /Accredited Wealth Steward logo as well, farther down the page is fine.

Thank you for your help! Feel free to contact me with any questions.

Target Market(s)

Individuals aged 48-62 who are looking to maximize their wealth, such as business owners, executives, engineers, successful tradespeople, etc.

Industry/Entity Type

Finance--wealth management

Font styles to use
Sans Serif

Requirements
Must have
• Professional and polished, Call to action buttons must be clear and stand out, headlines must be clear and stand out, also text must be big enough to be easily readable by most people
Should not have
• Anything casual, frilly, etc.

```html
<!DOCTYPE html>
<html lang="en">
<head>
<meta charset="utf-8">
<title>Meridale Asset Advisors — Home Page Design</title>
<link href="https://fonts.googleapis.com/css2?family=Heebo:wght@300;400;500;700&family=Playfair+Display:wght@400;700&display=swap" rel="stylesheet">
<style>
:root{
  --navy:#283b91;
  --coral:#ef5741;
  --paper:#f7f7f7;
  --board:#e7e9f2;
  --ink:#4a4d5c;
  --muted:#6b6f80;
  --hero-a:#a3b3ea;
  --hero-b:#6a80d6;
  --white:#ffffff;
}
*{box-sizing:border-box;margin:0;padding:0}
html,body{width:1200px;height:3482px;overflow:hidden}
body{background:var(--board);font-family:'Heebo',sans-serif;color:var(--ink);position:relative}
.abs{position:absolute}

/* Board header */
.brand-mark{position:absolute;left:257px;top:146px;display:flex;align-items:center;gap:9px}
.brand-mark .dot{width:30px;height:30px;border-radius:50%;background:var(--navy)}
.brand-mark .name{font-family:'Playfair Display',serif;color:var(--navy);font-size:17px;line-height:1;font-weight:400;white-space:nowrap}
.board-divider{position:absolute;top:122px;width:1px;height:90px;background:#b8bccb}
.board-label{position:absolute;top:118px;font-family:'Playfair Display',serif;color:var(--navy);font-size:22px}
.font-list{position:absolute;left:573px;top:162px;font-size:17px;color:#555a6b;line-height:26px}
.font-list .pf{font-family:'Playfair Display',serif}
.swatch{position:absolute;top:152px;width:38px;height:38px;border-radius:50%}
.swatch-code{position:absolute;top:197px;font-size:8px;color:#555a6b;width:60px;text-align:center}
.vertical-label{position:absolute;font-size:22px;letter-spacing:10px;color:var(--navy);font-weight:300;transform:rotate(-90deg);transform-origin:left top;white-space:nowrap}

/* Preview screens */
.screen{position:absolute;overflow:hidden;background:var(--hero-b)}
.scaler{position:absolute;left:0;top:0;transform-origin:left top}

/* Shared */
.topbar{height:19px;background:var(--navy);position:relative}
.social{position:absolute;top:6px;display:flex;gap:6px}
.social i{display:block;width:7px;height:7px;border-radius:50%;background:var(--white)}
.btn{position:absolute;background:var(--coral);color:var(--white);font-size:7px;font-weight:500;display:flex;align-items:center;justify-content:center;gap:5px;white-space:nowrap}
.btn svg{width:9px;height:5px}
.photo{position:absolute}
.link{color:var(--navy);text-decoration:underline}

/* Desktop page */
.page-desktop{position:absolute;left:158px;top:859px;width:669px;height:2497px;background:var(--white);overflow:hidden}
.hero{position:relative;height:450px;background:linear-gradient(160deg,var(--hero-a) 0%,#8a9de2 45%,var(--hero-b) 100%)}
.hero .visual{position:absolute;left:0;top:0;width:100%;height:100%;background:radial-gradient(ellipse at 76% 40%,rgba(255,255,255,.35) 0%,rgba(255,255,255,0) 40%)}
.site-nav{position:absolute;left:0;top:0;width:100%;height:61px;background:rgba(255,255,255,.12)}
.logo{position:absolute;display:flex;align-items:center;gap:6px}
.logo .dot{border-radius:50%;background:var(--white)}
.logo .name{font-family:'Playfair Display',serif;color:var(--white);line-height:1;white-space:nowrap}
.site-nav .logo{left:90px;top:20px}
.site-nav .logo .dot{width:20px;height:20px}
.site-nav .logo .name{font-size:12px}
.menu{position:absolute;top:25px;font-size:7px;color:var(--white)}
.hero h1{position:absolute;left:90px;top:155px;font-family:'Playfair Display',serif;font-weight:400;color:var(--white);font-size:25px;line-height:29px;width:260px}
.hero .lede{position:absolute;left:90px;top:267px;width:290px;font-size:7px;line-height:14px;color:var(--white)}

.intro{position:relative;height:226px;background:var(--white)}
.intro h2{position:absolute;left:90px;top:54px;width:215px;font-family:'Playfair Display',serif;font-weight:400;font-size:19px;line-height:25.5px;color:var(--navy)}
.intro p{position:absolute;left:382px;top:47px;width:205px;font-size:7px;line-height:14.3px;color:var(--ink)}

.features{position:relative;height:1009px;background:var(--paper)}
.section-title{position:absolute;left:0;width:100%;text-align:center;font-family:'Playfair Display',serif;font-weight:400;color:var(--navy)}
.section-sub{position:absolute;left:0;width:100%;text-align:center;font-size:7px;color:var(--ink)}
.feature-box{position:absolute;padding:23px 24px;font-size:6.5px;line-height:14px}
.feature-box h3{font-family:'Playfair Display',serif;font-weight:400;font-size:14px;margin-bottom:10px}
.feature-box.light{background:var(--white);color:var(--ink);box-shadow:0 2px 10px rgba(40,59,145,.08)}
.feature-box.light h3{color:var(--navy)}
.feature-box.dark{background:var(--navy);color:#dfe4f7}
.feature-box.dark h3{color:var(--white)}
.feature-box.dark .link{color:#fff}

.solutions{position:relative;height:202px;background:var(--white)}
.service{position:absolute;top:100px;width:100px;margin-left:-50px;text-align:center;font-size:6.5px;line-height:9px;color:var(--navy)}
.service svg{width:26px;height:26px;display:block;margin:0 auto 5px}

.checkup{position:relative;height:308px;background:var(--white)}
.checkup .band{position:absolute;left:245px;top:0;right:0;bottom:0;background:var(--navy)}
.checkup h2{position:absolute;left:341px;top:24px;width:250px;font-family:'Playfair Display',serif;font-weight:700;color:var(--white);font-size:18px;line-height:26px}
.checkup p{position:absolute;left:341px;top:124px;width:240px;font-size:6.5px;line-height:14px;color:#dfe4f7}

.site-footer{position:relative;height:261px;background:var(--paper)}
.footer-head{position:absolute;font-family:'Playfair Display',serif;font-size:11px;color:var(--navy);font-weight:400}
.footer-text{position:absolute;font-size:6.5px;line-height:14px;color:var(--ink)}
.footer-links{position:absolute;list-style:none;font-size:6.5px;color:var(--ink)}
.badge{position:absolute;border:1.5px solid #222;background:var(--white)}
.legal-bar{position:relative;height:22px;background:var(--navy);font-size:5.5px;color:#dfe4f7}
.legal-bar span{position:absolute;top:8px}

/* Mobile page */
.page-mobile{position:absolute;left:950px;top:859px;width:147px;height:2497px;background:var(--white);overflow:hidden}
.m-hero{position:relative;height:294px;background:linear-gradient(165deg,var(--hero-a) 0%,#8093dd 50%,var(--hero-b) 100%)}
.m-nav{position:absolute;left:0;top:0;width:100%;height:44px;background:rgba(255,255,255,.12)}
.m-nav .logo{left:9px;top:15px}
.m-nav .logo .dot{width:13px;height:13px}
.m-nav .logo .name{font-size:8px}
.burger{position:absolute;left:131px;top:20px;width:8px}
.burger i{display:block;height:1px;background:#fff;margin-bottom:2px}
.m-hero h1{position:absolute;left:9px;top:89px;width:120px;font-family:'Playfair Display',serif;font-weight:400;color:#fff;font-size:11.5px;line-height:17.5px}
.m-hero .lede{position:absolute;left:9px;top:155px;width:128px;font-size:4.6px;line-height:9px;color:#fff}
.m-btn{font-size:4.5px;gap:3px}
.m-btn svg{width:6px;height:4px}
.m-section{position:relative}
.m-h2{position:absolute;left:9px;width:128px;font-family:'Playfair Display',serif;font-weight:400;color:var(--navy);font-size:10.5px;line-height:15px}
.m-h2.small{font-size:8.5px;line-height:15px}
.m-text{position:absolute;left:9px;width:128px;font-size:4.4px;line-height:8.6px;color:var(--ink)}
.m-card{position:absolute;left:9px;width:129px;padding:12px 13px;font-size:4.2px;line-height:8.4px}
.m-card h3{font-family:'Playfair Display',serif;font-weight:400;font-size:8.5px;margin-bottom:8px}
.m-card.light{background:#fff;color:var(--ink)}
.m-card.light h3{color:var(--navy)}
.m-card.dark{background:var(--navy);color:#dfe4f7}
.m-card.dark h3{color:#fff}
.m-card.dark .link{color:#fff}
.m-service{position:absolute;left:9px;font-size:4.2px;color:var(--navy)}
.m-service svg{width:18px;height:18px;display:block;margin-bottom:4px}
</style>
</head>
<body>

<!-- Board header -->
<div class="brand-mark"><span class="dot"></span><span class="name">Meridale Asset Advisors</span></div>
<div class="board-divider" style="left:513px"></div>
<div class="board-label" style="left:573px">Fonts:</div>
<div class="font-list"><div class="pf">Playfair Display</div><div>Heebo</div></div>
<div class="board-divider" style="left:759px"></div>
<div class="board-label" style="left:817px">Colors:</div>
<span class="swatch" style="left:819px;background:var(--navy)"></span>
<span class="swatch" style="left:866px;background:var(--coral)"></span>
<span class="swatch" style="left:912px;background:var(--paper)"></span>
<span class="swatch-code" style="left:808px">#283b91</span>
<span class="swatch-code" style="left:855px">#ef5741</span>
<span class="swatch-code" style="left:901px">#f7f7f7</span>

<!-- Flat screen previews -->
<div class="screen" style="left:351px;top:308px;width:588px;height:327px">
  <div class="scaler" style="width:669px;transform:scale(0.879)">
    <div class="topbar"><div class="social" style="left:562px"><i></i><i></i></div></div>
    <div class="hero">
      <div class="visual" role="img" aria-label="Photo of a calculator falling against a soft blue backdrop"></div>
      <nav class="site-nav">
        <div class="logo"><span class="dot"></span><span class="name">Meridale Asset Advisors</span></div>
        <span class="menu" style="left:263px">Who We Are</span><span class="menu" style="left:319px">Services</span><span class="menu" style="left:365px">News</span><span class="menu" style="left:399px">Contact</span>
        <span class="btn" style="left:515px;top:19px;width:72px;height:24px;font-size:6px">CLIENT LOGIN</span>
      </nav>
      <h1>The most effective financial plans start with tax planning.</h1>
      <p class="lede">Few financial advisors offer tax expertise, but when they do, you benefit. Learn how our unique team combines financial planning, investments and smart tax and income generation strategies to help you achieve your goals faster.</p>
      <span class="btn" style="left:90px;top:326px;width:117px;height:27px">Learn Why We're Different <svg viewBox="0 0 9 5"><path d="M0 2.5h8M6 .5l2 2-2 2" stroke="#fff" fill="none" stroke-width=".8"/></svg></span>
    </div>
  </div>
</div>

<div class="screen" style="left:159px;top:551px;width:365px;height:226px">
  <div class="scaler" style="width:669px;transform:scale(0.546)">
    <div class="topbar"><div class="social" style="left:562px"><i></i><i></i></div></div>
    <div class="hero">
      <div class="visual" role="img" aria-label="Photo of a calculator falling against a soft blue backdrop"></div>
      <nav class="site-nav">
        <div class="logo"><span class="dot"></span><span class="name">Meridale Asset Advisors</span></div>
        <span class="menu" style="left:263px">Who We Are</span><span class="menu" style="left:319px">Services</span><span class="menu" style="left:365px">News</span><span class="menu" style="left:399px">Contact</span>
        <span class="btn" style="left:515px;top:19px;width:72px;height:24px;font-size:6px">CLIENT LOGIN</span>
      </nav>
      <h1>The most effective financial plans start with tax planning.</h1>
      <p class="lede">Few financial advisors offer tax expertise, but when they do, you benefit. Learn how our unique team combines financial planning, investments and smart tax and income generation strategies to help you achieve your goals faster.</p>
      <span class="btn" style="left:90px;top:326px;width:117px;height:27px">Learn Why We're Different <svg viewBox="0 0 9 5"><path d="M0 2.5h8M6 .5l2 2-2 2" stroke="#fff" fill="none" stroke-width=".8"/></svg></span>
    </div>
  </div>
</div>

<div class="screen" style="left:962px;top:547px;width:126px;height:257px">
  <div class="scaler" style="width:147px;transform:scale(0.857)">
    <div class="topbar"><div class="social" style="left:124px;gap:4px;top:7px"><i style="width:5px;height:5px"></i><i style="width:5px;height:5px"></i></div></div>
    <div class="m-hero" role="img" aria-label="Photo of a calculator falling against a soft blue backdrop">
      <nav class="m-nav"><div class="logo"><span class="dot"></span><span class="name">Meridale</span></div><div class="burger"><i></i><i></i><i></i></div></nav>
      <h1>The most effective financial plans start with tax planning.</h1>
      <p class="lede">Few financial advisors offer tax expertise, but when they do, you benefit. Learn how our unique team combines financial planning, investments and smart tax and income generation strategies to help you achieve your goals faster.</p>
      <span class="btn m-btn" style="left:9px;top:227px;width:88px;height:16px">Learn Why We're Different <svg viewBox="0 0 9 5"><path d="M0 2.5h8M6 .5l2 2-2 2" stroke="#fff" fill="none" stroke-width=".8"/></svg></span>
    </div>
  </div>
</div>

<!-- Vertical labels -->
<div class="vertical-label" style="left:112px;top:2297px">LAPTOP / DESKTOP</div>
<div class="vertical-label" style="left:907px;top:2178px">MOBILE</div>

<!-- Desktop page -->
<main class="page-desktop">
  <div class="topbar"><div class="social" style="left:562px"><i></i><i></i></div></div>

  <header class="hero">
    <div class="visual" role="img" aria-label="Photo of a calculator falling against a soft blue backdrop"></div>
    <nav class="site-nav">
      <div class="logo"><span class="dot"></span><span class="name">Meridale Asset Advisors</span></div>
      <span class="menu" style="left:263px">Who We Are</span>
      <span class="menu" style="left:319px">Services</span>
      <span class="menu" style="left:365px">News</span>
      <span class="menu" style="left:399px">Contact</span>
      <span class="btn" style="left:515px;top:19px;width:72px;height:24px;font-size:6px">CLIENT LOGIN</span>
    </nav>
    <h1>The most effective financial plans start with tax planning.</h1>
    <p class="lede">Few financial advisors offer tax expertise, but when they do, you benefit. Learn how our unique team combines financial planning, investments and smart tax and income generation strategies to help you achieve your goals faster.</p>
    <span class="btn" style="left:90px;top:326px;width:117px;height:27px">Learn Why We're Different <svg viewBox="0 0 9 5"><path d="M0 2.5h8M6 .5l2 2-2 2" stroke="#fff" fill="none" stroke-width=".8"/></svg></span>
  </header>

  <section class="intro">
    <h2>Cookie-cutter financial planning and investment can leave your future at risk. That's why we do it differently.</h2>
    <p>You need better strategies in today's complex financial landscape. At Meridale Asset Advisors, we bring financial planning, investment management, retirement income, tax and estate planning expertise together under one roof. Our unique team works together to help you make the most of your resources.</p>
    <span class="btn" style="left:382px;top:148px;width:118px;height:28px">Meet Our Specialists <svg viewBox="0 0 9 5"><path d="M0 2.5h8M6 .5l2 2-2 2" stroke="#fff" fill="none" stroke-width=".8"/></svg></span>
  </section>

  <section class="features">
    <h2 class="section-title" style="top:50px;font-size:16.5px;line-height:26px;padding:0 110px">Better strategies to preserve and grow wealth, generate income and reduce your taxes</h2>
    <p class="section-sub" style="top:113px">Here's what you can expect when you work with Meridale.</p>

    <div class="photo" style="left:90px;top:145px;width:322px;height:254px;background:linear-gradient(135deg,#d9dde6,#8e96c9 60%,#5a66b0)" role="img" aria-label="Photo of a woman reviewing paperwork at a laptop"></div>
    <div class="feature-box light" style="left:342px;top:179px;width:236px;height:185px">
      <h3>A Better Approach</h3>
      Taxes are critical to every financial move you make, so we incorporate tax planning in everything we do for you. Along with managing your investments, we help you <span class="link">safely generate retirement income, reduce capital gains and minimize income taxes.</span> We'll also help you with estate planning strategies so you can protect your family's future and make the most of opportunities.
    </div>

    <div class="photo" style="left:258px;top:426px;width:322px;height:253px;background:linear-gradient(135deg,#eef0f3,#c4c7cf 50%,#6b6f80)" role="img" aria-label="Photo of the advisory team standing together in an office"></div>
    <div class="feature-box dark" style="left:90px;top:459px;width:238px;height:186px">
      <h3>More Experience</h3>
      You've worked hard to get where you are, so your money shouldn't have to be part of anyone's learning curve. At Meridale Asset Advisors, you'll only work with <span class="link">seasoned experts</span>, each with decades of investment, planning or tax experience. Our team works together to help solve your financial challenges and get your money working harder for you.
    </div>

    <div class="photo" style="left:90px;top:705px;width:322px;height:254px;background:linear-gradient(135deg,#e4e6ea,#a8b0c6 55%,#4c5a8e)" role="img" aria-label="Photo of a retired couple meeting with an advisor at a laptop"></div>
    <div class="feature-box light" style="left:342px;top:739px;width:236px;height:186px">
      <h3>On Your Side</h3>
      In an industry rife with conflicts of interest, you need a firm that works in your <span class="link">best interest</span>. As an independent firm, we have no ties to insurance or mutual fund companies. <span class="link">We're fee-based</span>, meaning we're <span class="link">compensated by fees, not commissions</span>. We also act as your fiduciary, so we're ethically bound to put your interests first. That way, you get our best advice...not product recommendations.
    </div>
  </section>

  <section class="solutions">
    <h2 class="section-title" style="top:50px;font-size:16.5px">Personalized solutions to help your money work harder for you</h2>
    <div class="service" style="left:130px"><svg viewBox="0 0 26 26" fill="none" stroke="var(--coral)" stroke-width="1.3"><path d="M3 22h20M6 22v-6M11 22v-9M16 22v-5M21 22v-12M5 12l6-5 5 3 6-6"/></svg>Investment Management</div>
    <div class="service" style="left:257px"><svg viewBox="0 0 26 26" fill="none" stroke="var(--coral)" stroke-width="1.3"><path d="M6 2h11l4 4v18H6z"/><path d="M9 9h9M9 13h9M9 17h6"/></svg>Comprehensive Financial<br>Planning</div>
    <div class="service" style="left:370px"><svg viewBox="0 0 26 26" fill="none" stroke="var(--coral)" stroke-width="1.3"><rect x="5" y="2" width="16" height="22"/><circle cx="13" cy="11" r="4"/><path d="M9 19h8"/></svg>Retirement Income<br>Planning</div>
    <div class="service" style="left:465px"><svg viewBox="0 0 26 26" fill="none" stroke="var(--coral)" stroke-width="1.3"><rect x="4" y="3" width="18" height="20"/><path d="M7 7h12M8 12h2M12 12h2M16 12h2M8 16h2M12 16h2M16 16h2M8 20h10"/></svg>Tax Planning</div>
    <div class="service" style="left:554px"><svg viewBox="0 0 26 26" fill="none" stroke="var(--coral)" stroke-width="1.3"><circle cx="13" cy="13" r="4"/><circle cx="4" cy="4" r="2.5"/><circle cx="22" cy="4" r="2.5"/><circle cx="4" cy="22" r="2.5"/><circle cx="22" cy="22" r="2.5"/><path d="M6 6l4 4M20 6l-4 4M6 20l4-4M20 20l-4-4"/></svg>Estate Planning</div>
  </section>

  <section class="checkup">
    <div class="band"></div>
    <div class="photo" style="left:90px;top:50px;width:213px;height:203px;background:linear-gradient(135deg,#efe3d6,#d8a488 55%,#b0705a)" role="img" aria-label="Photo of a couple reviewing retirement documents together"></div>
    <h2 style="top:64px">The Meridale $549 Retirement Check-Up</h2>
    <p style="top:132px">We know it's a big decision to hire or switch advisors. That's why we provide an easy way to try us out. At the same time, you can get a valuable second opinion to find out if you're on track to retire. There's no pressure, and either way, you'll walk away with valuable insights on what you should be doing to secure your future.</p>
    <span class="btn" style="left:341px;top:215px;width:117px;height:27px">Learn more about check-up <svg viewBox="0 0 9 5"><path d="M0 2.5h8M6 .5l2 2-2 2" stroke="#fff" fill="none" stroke-width=".8"/></svg></span>
  </section>

  <footer class="site-footer">
    <h4 class="footer-head" style="left:90px;top:51px">About Meridale Asset Advisors</h4>
    <p class="footer-text" style="left:90px;top:82px;width:225px">With over 55 years of combined experience, Meridale Asset Advisors helps successful people more effectively prepare for the future. Our unique small team of wealth managers, financial planners and tax professionals bring you the strategies you need to preserve your wealth, minimize your taxes and create a confident retirement. While we're based in Harlow County, Westmark, we serve clients nationwide.</p>
    <div class="badge" style="left:90px;top:199px;width:70px;height:18px" role="img" aria-label="Accredited Wealth Steward badge"></div>
    <h4 class="footer-head" style="left:370px;top:51px">Quick Links</h4>
    <ul class="footer-links" style="left:370px;top:78px;line-height:22px"><li>Home</li><li>Who We Are</li><li>Services</li><li>News</li><li>Contact</li></ul>
    <h4 class="footer-head" style="left:516px;top:51px">Follow Us</h4>
    <div class="social" style="left:516px;top:79px"><i style="background:var(--navy)"></i><i style="background:var(--navy)"></i></div>
  </footer>

  <div class="legal-bar"><span style="left:90px">Copyright © 2021 · Meridale Asset Advisors · All rights reserved</span><span style="right:90px">Privacy Policy | Site Map</span></div>
</main>

<!-- Mobile page -->
<main class="page-mobile">
  <div class="topbar"><div class="social" style="left:124px;gap:4px;top:7px"><i style="width:5px;height:5px"></i><i style="width:5px;height:5px"></i></div></div>

  <header class="m-hero" role="img" aria-label="Photo of a calculator falling against a soft blue backdrop">
    <nav class="m-nav"><div class="logo"><span class="dot"></span><span class="name">Meridale</span></div><div class="burger"><i></i><i></i><i></i></div></nav>
    <h1>The most effective financial plans start with tax planning.</h1>
    <p class="lede">Few financial advisors offer tax expertise, but when they do, you benefit. Learn how our unique team combines financial planning, investments and smart tax and income generation strategies to help you achieve your goals faster.</p>
    <span class="btn m-btn" style="left:9px;top:227px;width:88px;height:16px">Learn Why We're Different <svg viewBox="0 0 9 5"><path d="M0 2.5h8M6 .5l2 2-2 2" stroke="#fff" fill="none" stroke-width=".8"/></svg></span>
  </header>

  <section class="m-section" style="height:192px;background:#fff">
    <h2 class="m-h2" style="top:24px">Cookie-cutter financial planning and investment can leave your future at risk. That's why we do it differently.</h2>
    <p class="m-text" style="top:117px">You need better strategies in today's complex financial landscape. At Meridale Asset Advisors, we bring financial planning, investment management, retirement income, tax and estate planning expertise together under one roof. Our unique team works together to help you make the most of your resources.</p>
  </section>

  <section class="m-section" style="height:932px;background:var(--paper)">
    <h2 class="m-h2 small" style="top:40px">Better strategies to preserve and grow wealth, generate income and reduce your taxes</h2>
    <p class="m-text" style="top:100px">Here's what you can expect when you work with Meridale.</p>

    <div class="photo" style="left:9px;top:151px;width:129px;height:89px;background:linear-gradient(135deg,#d9dde6,#8e96c9 60%,#5a66b0)" role="img" aria-label="Photo of a woman reviewing paperwork at a laptop"></div>
    <div class="m-card light" style="top:240px;height:149px"><h3>A Better Approach</h3>Taxes are critical to every financial move you make, so we incorporate tax planning in everything we do for you. Along with managing your investments, we help you <span class="link">safely generate retirement income, reduce capital gains and minimize income taxes.</span> We'll also help you with estate planning strategies so you can protect your family's future and make the most of opportunities.</div>

    <div class="photo" style="left:9px;top:411px;width:129px;height:92px;background:linear-gradient(135deg,#eef0f3,#c4c7cf 50%,#6b6f80)" role="img" aria-label="Photo of the advisory team standing together in an office"></div>
    <div class="m-card dark" style="top:503px;height:151px"><h3>More Experience</h3>You've worked hard to get where you are, so your money shouldn't have to be part of anyone's learning curve. At Meridale Asset Advisors, you'll only work with <span class="link">seasoned experts</span>, each with decades of investment, planning or tax experience. Our team works together to help solve your financial challenges and get your money working harder for you.</div>

    <div class="photo" style="left:9px;top:671px;width:129px;height:92px;background:linear-gradient(135deg,#e4e6ea,#a8b0c6 55%,#4c5a8e)" role="img" aria-label="Photo of a retired couple meeting with an advisor at a laptop"></div>
    <div class="m-card light" style="top:763px;height:152px"><h3>On Your Side</h3>In an industry rife with conflicts of interest, you need a firm that works in your <span class="link">best interest</span>. As an independent firm, we have no ties to insurance or mutual fund companies. <span class="link">We're fee-based</span>, meaning we're <span class="link">compensated by fees, not commissions</span>. We also act as your fiduciary, so we're ethically bound to put your interests first. That way, you get our best advice...not product recommendations.</div>
  </section>

  <section class="m-section" style="height:331px;background:#fff">
    <h2 class="m-h2 small" style="top:40px">Personalized solutions to help your money work harder for you</h2>
    <div class="m-service" style="top:94px"><svg viewBox="0 0 26 26" fill="none" stroke="var(--coral)" stroke-width="1.3"><path d="M3 22h20M6 22v-6M11 22v-9M16 22v-5M21 22v-12M5 12l6-5 5 3 6-6"/></svg>Investment Management</div>
    <div class="m-service" style="top:141px"><svg viewBox="0 0 26 26" fill="none" stroke="var(--coral)" stroke-width="1.3"><path d="M6 2h11l4 4v18H6z"/><path d="M9 9h9M9 13h9M9 17h6"/></svg>Comprehensive Financial Planning</div>
    <div class="m-service" style="top:188px"><svg viewBox="0 0 26 26" fill="none" stroke="var(--coral)" stroke-width="1.3"><rect x="5" y="2" width="16" height="22"/><circle cx="13" cy="11" r="4"/><path d="M9 19h8"/></svg>Retirement Income Planning</div>
    <div class="m-service" style="top:235px"><svg viewBox="0 0 26 26" fill="none" stroke="var(--coral)" stroke-width="1.3"><rect x="4" y="3" width="18" height="20"/><path d="M7 7h12M8 12h2M12 12h2M16 12h2M8 16h2M12 16h2M16 16h2M8 20h10"/></svg>Tax Planning</div>
    <div class="m-service" style="top:282px"><svg viewBox="0 0 26 26" fill="none" stroke="var(--coral)" stroke-width="1.3"><circle cx="13" cy="13" r="4"/><circle cx="4" cy="4" r="2.5"/><circle cx="22" cy="4" r="2.5"/><circle cx="4" cy="22" r="2.5"/><circle cx="22" cy="22" r="2.5"/><path d="M6 6l4 4M20 6l-4 4M6 20l4-4M20 20l-4-4"/></svg>Estate Planning</div>
  </section>

  <section class="m-section" style="height:345px;background:#fff">
    <div class="abs" style="left:0;top:98px;width:147px;height:247px;background:var(--navy)"></div>
    <div class="photo" style="left:9px;top:33px;width:129px;height:122px;background:linear-gradient(135deg,#efe3d6,#d8a488 55%,#b0705a)" role="img" aria-label="Photo of a couple reviewing retirement documents together"></div>
    <h2 class="m-h2 small" style="top:170px;color:#fff;font-weight:700">The Meridale $549 Retirement Check-Up</h2>
    <p class="m-text" style="top:212px;color:#dfe4f7">We know it's a big decision to hire or switch advisors. That's why we provide an easy way to try us out. At the same time, you can get a valuable second opinion to find out if you're on track to retire. There's no pressure, and either way, you'll walk away with valuable insights on what you should be doing to secure your future.</p>
    <span class="btn m-btn" style="left:9px;top:302px;width:90px;height:20px">Learn more about check-up <svg viewBox="0 0 9 5"><path d="M0 2.5h8M6 .5l2 2-2 2" stroke="#fff" fill="none" stroke-width=".8"/></svg></span>
  </section>

  <footer class="m-section" style="height:362px;background:var(--paper)">
    <h4 class="footer-head" style="left:9px;top:33px;font-size:8px">About Meridale Asset Advisors</h4>
    <p class="m-text" style="top:53px">With over 55 years of combined experience, Meridale Asset Advisors helps successful people more effectively prepare for the future. Our unique small team of wealth managers, financial planners and tax professionals bring you the strategies you need to preserve your wealth, minimize your taxes and create a confident retirement. While we're based in Harlow County, Westmark, we serve clients nationwide.</p>
    <div class="badge" style="left:9px;top:159px;width:54px;height:14px;border-width:1px" role="img" aria-label="Accredited Wealth Steward badge"></div>
    <h4 class="footer-head" style="left:9px;top:184px;font-size:8px">Quick Links</h4>
    <ul class="footer-links" style="left:9px;top:206px;font-size:4.4px;line-height:16.5px"><li>Home</li><li>Who We Are</li><li>Services</li><li>News</li><li>Contact</li></ul>
    <h4 class="footer-head" style="left:9px;top:295px;font-size:8px">Follow Us</h4>
    <div class="social" style="left:9px;top:318px;gap:4px"><i style="width:5px;height:5px;background:var(--navy)"></i><i style="width:5px;height:5px;background:var(--navy)"></i></div>
  </footer>

  <div class="legal-bar" style="height:21px;font-size:3.6px;text-align:center">
    <span style="left:0;width:100%;top:5px">Copyright © 2021 · Meridale Asset Advisors · All rights reserved</span>
    <span style="left:0;width:100%;top:12px">Privacy Policy | Site Map</span>
  </div>
</main>

</body>
</html>
```